Logo Design with Business Card Project

Attractive Logo with colourful background !
I have uploaded a new image of the updated Home page with the Real Estate landing page for your reference.
We are looking for a Business card design which easily identifies us as a Video classifieds company.

Target Market(s)

20 - 35 yr old people who are connected through social media

Industry/Entity Type

Business

Logo Text

WE SEE ALL

Logo styles of interest
Abstract Logo
Requirements
Must have
• Simple layout with striking / engaging colours
Nice to have
• Require an updated logo to go on business card / home page

```html
<!DOCTYPE html>
<html lang="en">
<head>
<meta charset="utf-8">
<title>WE SEE ALL – Business Card</title>
<link rel="stylesheet" href="https://fonts.googleapis.com/css2?family=Questrial&family=Arimo:wght@400;700&display=swap">
<style>
  :root {
    --stage: #1c1c1c;
    --card-dark: #121212;
    --card-light: #ffffff;
    --ink-light: #ffffff;
    --ink-dark: #1a1a1a;
    --accent-blue: #2a7fd4;
    --accent-orange: #f5a000;
    --badge-grey: #9a9a9a;
  }
  * { margin: 0; padding: 0; box-sizing: border-box; }
  html, body {
    width: 1200px; height: 816px; overflow: hidden;
    background: var(--stage);
  }
  .stage {
    position: relative; width: 1200px; height: 816px;
    display: flex; align-items: center; justify-content: center; gap: 60px;
  }
  .card {
    position: relative; width: 520px; height: 300px;
    border-radius: 4px;
    box-shadow: 0 12px 30px rgba(0,0,0,.5);
  }
  .card--front { background: var(--card-dark); color: var(--ink-light); }
  .card--back { background: var(--card-light); color: var(--ink-dark); }

  .wordmark {
    font-family: "Questrial", sans-serif;
    font-size: 34px; letter-spacing: 1px; line-height: 1;
    display: flex; align-items: center; gap: 10px;
  }
  .wordmark__mark { width: 14px; height: 14px; border-radius: 50%; }
  .card--front .wordmark { position: absolute; left: 34px; top: 52px; color: var(--ink-light); }
  .card--front .wordmark__mark { background: var(--accent-orange); }
  .card--back .wordmark {
    position: absolute; left: 0; right: 0; top: 96px;
    justify-content: center; color: var(--ink-dark);
  }
  .card--back .wordmark__mark { background: var(--accent-orange); }

  .tagline { font-family: "Arimo", sans-serif; line-height: 1.25; }
  .card--front .tagline {
    position: absolute; left: 34px; top: 112px;
    font-size: 16px; font-weight: 700;
  }
  .card--front .tagline__highlight { color: var(--accent-blue); }
  .card--back .tagline {
    position: absolute; left: 0; right: 0; top: 150px;
    text-align: center; font-size: 19px; font-weight: 400;
  }
  .card--back .tagline__highlight { color: var(--accent-orange); }

  .person { position: absolute; right: 34px; top: 118px; text-align: right; }
  .person__name { font-family: "Questrial", sans-serif; font-size: 19px; letter-spacing: .5px; }
  .person__role { font-family: "Arimo", sans-serif; font-size: 13px; font-weight: 700; color: var(--accent-orange); margin-top: 2px; }

  .contacts {
    position: absolute; left: 290px; top: 196px; list-style: none;
    font-family: "Arimo", sans-serif; font-size: 13px; font-weight: 700; letter-spacing: 1px;
  }
  .contacts__item { display: flex; align-items: center; gap: 8px; height: 20px; }
  .contacts__badge {
    width: 15px; height: 15px; border-radius: 50%;
    background: var(--badge-grey); color: var(--ink-light);
    font-size: 9px; display: flex; align-items: center; justify-content: center; letter-spacing: 0;
  }
</style>
</head>
<body>
<main class="stage">
  <article class="card card--front">
    <div class="wordmark"><span class="wordmark__mark"></span><span class="wordmark__name">WE SEE ALL</span></div>
    <p class="tagline">Buy and sell through the<br><span class="tagline__highlight">#1 Video Classifieds</span></p>
    <div class="person">
      <p class="person__name">Daniel Hartwell</p>
      <p class="person__role">Managing Director</p>
    </div>
    <ul class="contacts">
      <li class="contacts__item"><span class="contacts__badge">E</span>daniel@weseeall.com</li>
      <li class="contacts__item"><span class="contacts__badge">W</span>www.weseeall.com</li>
      <li class="contacts__item"><span class="contacts__badge">P</span>+617 5500 1234</li>
      <li class="contacts__item"><span class="contacts__badge">M</span>0400 555 019</li>
    </ul>
  </article>

  <article class="card card--back">
    <div class="wordmark"><span class="wordmark__mark"></span><span class="wordmark__name">WE SEE ALL</span></div>
    <p class="tagline">Buy and sell through the<br><span class="tagline__highlight">#1 Video Classifieds</span></p>
  </article>
</main>
</body>
</html>
```